Cedar Basin CBD Apothecary needs label for CBD capsule bottles

I need a 1 1/2"H x 3.5" W label for a cobalt blue glass pill bottle. Looking for apothecary look, but not over the top. I would like a yellow background (ccff00), or combination thereof, and my company logo/name, in addition to the text "PURE CBD CRYSTAL ISOLATE", Dietary Supplement, Ingredients: 99.1% Cannabidiol Crystal Isolate, Lab Tested, ZERO THC, NO FILLERS, Keep Out of Reach of Children, Serving Suggestion: Take one PlantaShell Daily, increase dosage as needed, Storage- cool dry place away from light and heat, www.cbcbdshop.com

Target Market(s)

Adults with health issues, all ages.

Industry/Entity Type

Health And Wellness

Font styles to use
Other font styles liked:
• similar to Algerian. Apothecary fonts.

Colors
fbee3d

Requirements
Must have
• Logo and Company name, "CEDAR BASIN CBD APOTHECARY"
• Yellow to contrast cobalt blue bottles
Nice to have
• Made in Joshua Tree, CA.
• Vegan Capsules
• NO GMO
Should not have
• no pot leaves or anything overtly cannabis related. No script fonts.

```html
<!DOCTYPE html>
<html lang="en">
<head>
<meta charset="utf-8">
<title>Cedar Basin CBD Apothecary – Capsule Labels</title>
<link rel="stylesheet" href="https://fonts.googleapis.com/css2?family=Cinzel:wght@400;700&display=swap">
<style>
  :root {
    --page: #ffffff;
    --slate-bg: #3c4b4d;
    --slate-ink: #c8b52c;
    --yellow-bg: #f8ec34;
    --yellow-ink: #161616;
    --paper-bg: #ededeb;
    --paper-ink: #1f1f1f;
  }
  * { box-sizing: border-box; margin: 0; padding: 0; }
  html, body { width: 1200px; height: 616px; overflow: hidden; background: var(--page); }
  .canvas { position: relative; width: 1200px; height: 616px; }

  .label {
    position: absolute;
    top: 178px;
    width: 222px;
    height: 252px;
    background: var(--bg);
    color: var(--ink);
    font-family: "Cinzel", "Times New Roman", serif;
  }
  .label--slate  { left: 87px;  --bg: var(--slate-bg);  --ink: var(--slate-ink); }
  .label--yellow { left: 489px; --bg: var(--yellow-bg); --ink: var(--yellow-ink); }
  .label--paper  { left: 885px; --bg: var(--paper-bg);  --ink: var(--paper-ink); }

  .label__frame {
    position: absolute;
    inset: 7px;
    border: 2px solid var(--ink);
  }
  .label__ornament {
    position: absolute;
    left: 14px;
    right: 14px;
    height: 12px;
    background: linear-gradient(90deg, var(--ink) 0 22%, transparent 22% 78%, var(--ink) 78%);
    opacity: 0.75;
  }
  .label__ornament--top { top: 14px; }
  .label__ornament--bottom { bottom: 14px; }

  .label__arc {
    position: absolute;
    left: 12px;
    top: 14px;
    width: 198px;
    height: 40px;
  }
  .label__mark {
    position: absolute;
    left: 72px;
    top: 52px;
    width: 78px;
    height: 78px;
    border: 2px solid var(--ink);
    border-radius: 50%;
  }

  .label__text {
    position: absolute;
    left: 0;
    right: 0;
    top: 150px;
    text-align: center;
    line-height: 1.1;
  }
  .label__name-top { font-size: 12px; font-weight: 400; letter-spacing: 0.5px; }
  .label__name-main { font-size: 19px; font-weight: 700; letter-spacing: 0.5px; }
  .label__origin { margin-top: 4px; font-size: 6px; font-weight: 700; letter-spacing: 0.3px; }
  .label__claim { margin-top: 4px; font-size: 6px; font-weight: 700; }
</style>
</head>
<body>
<main class="canvas">

  <section class="label label--slate">
    <div class="label__frame"></div>
    <div class="label__ornament label__ornament--top" role="img" aria-label="Decorative scroll flourishes in the top corners"></div>
    <svg class="label__arc" viewBox="0 0 198 40" aria-hidden="true"><path d="M8 34 Q99 -6 190 34" fill="none" stroke="currentColor" stroke-width="1.5"/></svg>
    <div class="label__mark"></div>
    <div class="label__text">
      <p class="label__name-top">CEDAR BASIN CBD</p>
      <p class="label__name-main">APOTHECARY</p>
      <p class="label__origin">MADE IN JOSHUA TREE, CA.</p>
      <p class="label__claim">NO GMO</p>
    </div>
    <div class="label__ornament label__ornament--bottom" role="img" aria-label="Decorative scroll flourishes in the bottom corners"></div>
  </section>

  <section class="label label--yellow">
    <div class="label__frame"></div>
    <div class="label__ornament label__ornament--top" role="img" aria-label="Decorative scroll flourishes in the top corners"></div>
    <svg class="label__arc" viewBox="0 0 198 40" aria-hidden="true"><path d="M8 34 Q99 -6 190 34" fill="none" stroke="currentColor" stroke-width="1.5"/></svg>
    <div class="label__mark"></div>
    <div class="label__text">
      <p class="label__name-top">CEDAR BASIN CBD</p>
      <p class="label__name-main">APOTHECARY</p>
      <p class="label__origin">MADE IN JOSHUA TREE, CA.</p>
      <p class="label__claim">NO GMO</p>
    </div>
    <div class="label__ornament label__ornament--bottom" role="img" aria-label="Decorative scroll flourishes in the bottom corners"></div>
  </section>

  <section class="label label--paper">
    <div class="label__frame"></div>
    <div class="label__ornament label__ornament--top" role="img" aria-label="Decorative scroll flourishes in the top corners"></div>
    <svg class="label__arc" viewBox="0 0 198 40" aria-hidden="true"><path d="M8 34 Q99 -6 190 34" fill="none" stroke="currentColor" stroke-width="1.5"/></svg>
    <div class="label__mark"></div>
    <div class="label__text">
      <p class="label__name-top">CEDAR BASIN CBD</p>
      <p class="label__name-main">APOTHECARY</p>
      <p class="label__origin">MADE IN JOSHUA TREE, CA.</p>
      <p class="label__claim">NO GMO</p>
    </div>
    <div class="label__ornament label__ornament--bottom" role="img" aria-label="Decorative scroll flourishes in the bottom corners"></div>
  </section>

</main>
</body>
</html>
```